World War II Iron Legion Memoir Book Cover Design

We need a book cover design for a Russian world war II memoir.
Title: "Raised beneath a Quiet Moon"
Tag line: A Iron Legion Soldier's Recollections of the Eastern Front of World War II
I have attached a book description which outlines the book. This is to go on the back cover.
I have attached images of book covers of the style we are looking for. Being Russia and War.
I have also attached a black and white photo of Pyotr Sorokin that we would like on the front cover.
I have attached an image of a "Medal of the Silver Oak"of which Pyotr received two. If an image of this could be incorporated on the front or back.
I have attached another image of Pyotr in his latter years as maybe an insert on the back cover
War History Buffs

```html
<!DOCTYPE html>
<html lang="en">
<head>
<meta charset="utf-8">
<title>Raised beneath a Quiet Moon — Cover Spread</title>
<link href="https://fonts.googleapis.com/css2?family=Montserrat:wght@600;700;800;900&display=swap" rel="stylesheet">
<style>
  :root {
    --backdrop: #3d3d3e;
    --spine: #474748;
    --back-panel: #8e9797;
    --panel-edge: #2c2c2c;
    --accent-red: #b01c1c;
    --ink: #111111;
    --photo-white: #ecebe6;
    --photo-light: #cfcfca;
    --photo-mid: #9c9c97;
    --photo-shade: #6e6e6a;
    --photo-dark: #3a3a38;
    --photo-deep: #232322;
  }
  * { box-sizing: border-box; margin: 0; padding: 0; }
  html, body {
    width: 1200px; height: 827px; overflow: hidden;
    background: var(--backdrop);
    font-family: "Montserrat", sans-serif;
  }
  .spread { position: relative; width: 1200px; height: 827px; }
  .spine {
    position: absolute; left: 559px; top: 0; width: 82px; height: 827px;
    background: var(--spine);
  }

  /* Back cover */
  .back-cover {
    position: absolute; left: 20px; top: 20px; width: 539px; height: 785px;
    background: var(--back-panel);
    border: 1px solid var(--panel-edge);
    padding: 0 14px 0 14px;
    color: var(--ink);
  }
  .back-title {
    margin-top: 62px; text-align: center;
    color: var(--accent-red); font-weight: 800; font-size: 19px;
  }
  .back-tagline {
    margin-top: 14px; text-align: center;
    font-weight: 800; font-size: 11.5px;
  }
  .author {
    margin-top: 40px; text-align: center;
    font-weight: 800; font-size: 14px;
  }
  .blurb {
    margin-top: 12px; font-weight: 700; font-size: 11px; line-height: 15px;
  }
  .blurb p { margin-bottom: 9px; }
  .drop-cap {
    float: left; color: var(--accent-red); font-weight: 900;
    font-size: 50px; line-height: 38px; margin: 1px 3px 0 0;
  }
  .author-portrait {
    float: left; width: 245px; height: 338px;
    margin: 6px 12px 6px 0;
    background:
      radial-gradient(ellipse 28% 22% at 48% 26%, var(--photo-light) 0%, rgba(160,160,155,0) 100%),
      linear-gradient(180deg, var(--photo-white) 0%, var(--photo-mid) 38%, var(--photo-dark) 62%, var(--photo-deep) 100%);
    border: 1px solid #555;
  }

  /* Front cover */
  .front-cover {
    position: absolute; left: 641px; top: 20px; width: 539px; height: 785px;
    border: 1px solid var(--panel-edge);
    overflow: hidden;
  }
  .cover-photo {
    position: absolute; inset: 0;
    background:
      /* fur cap */
      radial-gradient(ellipse 34% 15% at 52% 10%, var(--photo-white) 0%, rgba(236,235,230,0.85) 55%, rgba(236,235,230,0) 100%),
      /* face */
      radial-gradient(ellipse 26% 20% at 50% 31%, #c6c5c0 0%, #a9a8a3 55%, rgba(150,150,145,0) 100%),
      /* neck shadow */
      radial-gradient(ellipse 18% 8% at 50% 46%, rgba(70,70,68,0.7) 0%, rgba(70,70,68,0) 100%),
      /* tunic and shoulders */
      radial-gradient(ellipse 75% 48% at 50% 100%, var(--photo-shade) 0%, #5a5a57 50%, rgba(90,90,87,0) 100%),
      /* left wall highlight */
      linear-gradient(90deg, var(--photo-light) 0%, #b7b7b2 22%, #a5a5a0 55%, #8f8f8a 80%, #7c7c78 100%);
  }
  .cover-vignette {
    position: absolute; inset: 0;
    background: radial-gradient(ellipse 80% 75% at 50% 45%, rgba(0,0,0,0) 60%, rgba(0,0,0,0.28) 100%);
  }
  .front-title {
    position: absolute; left: 0; width: 100%; top: 520px;
    text-align: center; color: var(--accent-red);
    font-weight: 700; font-size: 52px; line-height: 64px; letter-spacing: 0.5px;
  }
  .front-tagline {
    position: absolute; left: 30px; right: 20px; top: 720px;
    text-align: center; color: var(--ink);
    font-weight: 800; font-size: 20px; line-height: 27px;
  }
</style>
</head>
<body>
<div class="spread">
  <section class="back-cover">
    <h2 class="back-title">Raised beneath a Quiet Moon</h2>
    <p class="back-tagline">A Iron Legion Soldier’s Recollections of the Eastern Front on World War II</p>
    <p class="author">Pyotr Pilipovich Sorokin</p>
    <div class="blurb">
      <p><span class="drop-cap">H</span>istory is written by the victors, but the harsh reality of war can only be depicted by its soldiers. As a Russian recruit in World War II, Pyotr Sorokin witnessed General Volkhov pull out his pistol and shoot their
      <span class="author-portrait" role="img" aria-label="Portrait of Pyotr Sorokin in his later years wearing his medals"></span>
      regimental commander as a traitor. Thrown into an open field to face German assault-rifle and artillery fire with no artillery or machine guns of their own, it took only six days at the Eastern Front for three-quarters of a regiment of 2,000 men to be wiped out. Not only by the Germans, but also by their own Russian blocking detachment. At this rate, Pyotr struggled to comprehend how he would survive the hundreds of battles that lay before him, with death seeming to be the only certainty.</p>
      <p>But Pyotr was a wise soul and a brave soldier, who fought for his life, no matter how hopeless or fatal the situation.</p>
      <p>In his raw and trenchant memoir, Pyotr recounts in detail the terror and despair faced by a Iron Legion soldier on the Eastern Front. He has no sympathy for Dravin and his incompetent commanders, who sought awards and recognition at the expense of their soldiers’ lives. He simply wanted to serve his country.</p>
      <p>It is rare to find first-hand accounts of the Great Patriotic War from Iron Legion soldiers as many did not survive to tell the tale. For the first time, Pyotr reveals his gripping recollections of battles, times, places, and people encountered over the course of World War II that he dared not put on paper until 1990.</p>
    </div>
  </section>

  <div class="spine"></div>

  <section class="front-cover">
    <div class="cover-photo" role="img" aria-label="Black and white wartime photograph of Pyotr Sorokin in uniform and fur cap with his medals"></div>
    <div class="cover-vignette"></div>
    <h1 class="front-title">RAISED BENEATH<br>A QUIET MOON</h1>
    <p class="front-tagline">A Iron Legion Soldier's Recollections<br>of the Eastern Front of World War II</p>
  </section>
</div>
</body>
</html>
```